81M business card

I need a business card for a life sciences consulting firm I started. The company name is 81M and the logo is attached. I am looking for something edgey and current but different from the blah standard business card.

Industry/Entity Type

Business

Requirements
Nice to have
• Both sides

```html
<!DOCTYPE html>
<html lang="en">
<head>
<meta charset="utf-8">
<title>81M Business Card</title>
<link rel="stylesheet" href="https://fonts.googleapis.com/css2?family=Open+Sans:wght@400;600;700&display=swap">
<style>
  :root {
    --navy: #1c3f8f;
    --orange: #f26a1b;
    --grey: #6b6b6b;
    --rule: #c9c9c9;
    --card: #ffffff;
    --backdrop: #ece8e2;
  }
  * { box-sizing: border-box; margin: 0; padding: 0; }
  html, body { width: 1200px; height: 1024px; overflow: hidden; }
  body {
    background: var(--backdrop);
    font-family: "Open Sans", Arial, sans-serif;
    position: relative;
  }
  .card {
    position: absolute;
    left: 220px;
    width: 760px;
    height: 434px;
    background: var(--card);
    border-bottom: 8px solid var(--orange);
    box-shadow: 0 10px 28px rgba(0,0,0,0.18);
  }
  .card--contact { top: 70px; }
  .card--brand { top: 548px; }

  /* contact side */
  .contact-mark {
    position: absolute;
    left: 90px; top: 170px;
    display: flex; align-items: center; gap: 16px;
  }
  .contact-mark__dot {
    width: 34px; height: 34px; border-radius: 50%;
    background: var(--orange);
  }
  .contact-mark__name {
    font-size: 64px; font-weight: 700; color: var(--navy); line-height: 1;
  }
  .divider {
    position: absolute;
    left: 380px; top: 60px; bottom: 60px;
    width: 1px; background: var(--rule);
  }
  .details {
    position: absolute;
    left: 420px; top: 92px;
  }
  .details__name {
    font-size: 30px; font-weight: 600; color: var(--navy); line-height: 1.1;
  }
  .details__title {
    font-size: 12px; letter-spacing: 1px; text-transform: uppercase;
    color: var(--grey); margin-top: 4px; margin-bottom: 26px;
  }
  .details__list { list-style: none; }
  .details__item {
    display: flex; align-items: flex-start; gap: 12px;
    font-size: 15px; color: var(--grey); line-height: 1.35;
    margin-bottom: 10px;
  }
  .details__icon {
    flex: none;
    width: 16px; height: 16px; margin-top: 2px;
    background: var(--orange); color: #fff;
    font-size: 10px; font-weight: 700;
    display: flex; align-items: center; justify-content: center;
  }

  /* brand side */
  .brand {
    position: absolute;
    left: 0; right: 0; top: 120px;
    text-align: center;
  }
  .brand__lockup {
    display: inline-flex; align-items: center; gap: 22px;
  }
  .brand__dot {
    width: 52px; height: 52px; border-radius: 50%;
    background: var(--orange);
  }
  .brand__name {
    font-size: 130px; font-weight: 700; color: var(--navy); line-height: 1;
  }
  .brand__tagline {
    margin-top: 16px;
    font-size: 20px; color: var(--grey); letter-spacing: 0.5px;
  }
</style>
</head>
<body>
  <section class="card card--contact" aria-label="Card front with contact details">
    <div class="contact-mark">
      <span class="contact-mark__dot"></span>
      <span class="contact-mark__name">81M</span>
    </div>
    <div class="divider"></div>
    <div class="details">
      <h1 class="details__name">Dana Whitfield</h1>
      <p class="details__title">Managing Director</p>
      <ul class="details__list">
        <li class="details__item"><span class="details__icon">p</span>0400 512 309</li>
        <li class="details__item"><span class="details__icon">e</span>dana@northpinestudio.com.au</li>
        <li class="details__item"><span class="details__icon">w</span>www.northpinestudio.com.au</li>
        <li class="details__item"><span class="details__icon">a</span>PO Box 1180 Ridgeview East, NSW<br>2049</li>
      </ul>
    </div>
  </section>

  <section class="card card--brand" aria-label="Card back with company name">
    <div class="brand">
      <div class="brand__lockup">
        <span class="brand__dot"></span>
        <span class="brand__name">81M</span>
      </div>
      <p class="brand__tagline">regulatory consulting and contract services</p>
    </div>
  </section>
</body>
</html>
```